terras letterhead

We would like to create a new letterhead that our company will use for proposals, invoices, statements and letters. Our company name is Terra-Vantage. We are a landscape design/build and landscape maintenance company. We have a web site Terra-Vantage.example where our logo (the leaf with the lettering within it only) is displayed.

Industry/Entity Type

Graphic Design

Requirements
Must have
• Address and info on our current letterhead (uploaded)
Nice to have
• We would like the design to look presentable in grey scale as well as color.
Should not have
• Do not want to infringe much on the normal useable area within the normal print areas.

```html
<!DOCTYPE html>
<html lang="en">
<head>
<meta charset="utf-8">
<title>Terra-Vantage Letterhead</title>
<link href="https://fonts.googleapis.com/css2?family=Marcellus+SC&family=PT+Sans&display=swap" rel="stylesheet">
<style>
  :root {
    --backdrop: #e8e6e1;
    --paper: #ffffff;
    --leaf-light: #b4cb8a;
    --leaf-dark: #1e4423;
    --ink: #2a2a2a;
  }
  * { margin: 0; padding: 0; box-sizing: border-box; }
  html, body {
    width: 963px; height: 1200px; overflow: hidden;
    background: var(--backdrop);
  }
  .letterhead {
    position: absolute; left: 83px; top: 78px;
    width: 793px; height: 1025px;
    background: var(--paper);
    box-shadow: 0 2px 10px rgba(0,0,0,0.18);
    overflow: hidden;
  }
  .letterhead__waves { position: absolute; inset: 0; }
  .brand-name {
    position: absolute; left: 35px; top: 104px;
    width: 290px; text-align: center;
    font-family: "Marcellus SC", serif;
    font-size: 24px; color: var(--leaf-dark);
    letter-spacing: 0.5px;
  }
  .address {
    position: absolute; right: 19px; top: 30px;
    text-align: right;
    font-family: "Marcellus SC", serif;
    font-size: 15.5px; line-height: 23px;
    color: var(--leaf-dark); letter-spacing: 0.6px;
  }
  .contact {
    position: absolute; left: 34px; top: 930px;
    list-style: none;
    font-family: "PT Sans", sans-serif;
    font-size: 13px; line-height: 18.5px; color: var(--ink);
  }
  .contact__item { display: flex; align-items: center; gap: 3px; }
  .contact__icon { width: 9px; height: 9px; flex: none; }
</style>
</head>
<body>
  <main class="letterhead">
    <svg class="letterhead__waves" width="793" height="1025" viewBox="0 0 793 1025" aria-hidden="true">
      <path d="M0,0 H793 V285 C745,185 640,120 460,55 C320,12 170,12 0,52 Z" fill="var(--leaf-light)"/>
      <path d="M0,52 C170,12 320,12 460,55 C640,120 745,185 793,285" fill="none" stroke="#ffffff" stroke-width="9"/>
      <path d="M0,52 C170,12 320,12 460,55 C640,120 745,185 793,285" fill="none" stroke="var(--leaf-dark)" stroke-width="5"/>
      <path d="M0,740 C60,860 200,930 420,975 C600,1010 720,1000 793,968 V1025 H0 Z" fill="var(--leaf-light)"/>
      <path d="M0,740 C60,860 200,930 420,975 C600,1010 720,1000 793,968" fill="none" stroke="#ffffff" stroke-width="9"/>
      <path d="M0,740 C60,860 200,930 420,975 C600,1010 720,1000 793,968" fill="none" stroke="var(--leaf-dark)" stroke-width="5"/>
    </svg>

    <div class="brand-name">Terra-Vantage</div>

    <address class="address">
      1185 Meadowbrook Lane<br>
      Cedar Hollow<br>
      NJ 07999
    </address>

    <ul class="contact">
      <li class="contact__item">
        <svg class="contact__icon" viewBox="0 0 10 10"><path d="M2,1 L4,1 L4.5,3 L3.4,3.8 C4,5.2 4.8,6 6.2,6.6 L7,5.5 L9,6 L9,8 C5,9 1,5 2,1 Z" fill="var(--ink)"/></svg>
        555-014-2260
      </li>
      <li class="contact__item">
        <svg class="contact__icon" viewBox="0 0 10 10"><rect x="2.5" y="1" width="5" height="3" fill="var(--ink)"/><rect x="1" y="4" width="8" height="5" rx="1" fill="var(--ink)"/></svg>
        555-014-2261
      </li>
      <li class="contact__item">
        <svg class="contact__icon" viewBox="0 0 10 10"><rect x="1" y="2.5" width="8" height="5.5" fill="var(--ink)"/><path d="M1,2.5 L5,5.5 L9,2.5" fill="none" stroke="#fff" stroke-width="0.8"/></svg>
        service@terra-vantage.example
      </li>
      <li class="contact__item">
        <svg class="contact__icon" viewBox="0 0 10 10"><circle cx="5" cy="5" r="4" fill="none" stroke="var(--ink)" stroke-width="1"/><ellipse cx="5" cy="5" rx="1.8" ry="4" fill="none" stroke="var(--ink)" stroke-width="0.8"/><line x1="1" y1="5" x2="9" y2="5" stroke="var(--ink)" stroke-width="0.8"/></svg>
        www.terra-vantage.example
      </li>
    </ul>
  </main>
</body>
</html>
```